the orbit dental works
Cards,Letterheads, Sticker, etc
Modern
Milton Crawshay
Suite 4, 61 Holloway Street
Bellmore NSW 2287
theorbitdental@fernmail.com.au
theorbitdental.com.au
Second Name; Judith Crawshay.
We also need a sticker to place on packaging to promote business

```html
<!DOCTYPE html>
<html lang="en">
<head>
<meta charset="utf-8">
<title>The Orbit Dental Works – DL Envelope</title>
<link rel="stylesheet" href="https://fonts.googleapis.com/css2?family=Open+Sans:wght@300;400;600&family=Exo+2:wght@400&family=Satisfy&display=swap">
<style>
  :root {
    --backdrop: #2b2d30;
    --brand-blue: #1fa3e8;
    --brand-blue-deep: #0f86d0;
    --brand-blue-light: #3cb6f2;
    --paper: #ffffff;
    --ink-grey: #4a4d52;
    --wash: #e9f0f8;
    --white: #ffffff;
  }
  * { margin: 0; padding: 0; box-sizing: border-box; }
  html, body {
    width: 1200px;
    height: 614px;
    overflow: hidden;
    background: var(--backdrop);
  }
  .stage {
    position: relative;
    width: 1200px;
    height: 614px;
  }
  .envelope {
    position: absolute;
    left: 67px;
    top: 72px;
    width: 1061px;
    height: 485px;
    background: var(--paper);
    overflow: hidden;
  }
  .brand-panel {
    position: absolute;
    left: 0;
    top: 0;
    width: 355px;
    height: 100%;
    background: linear-gradient(180deg, var(--brand-blue-light) 0%, var(--brand-blue) 55%, var(--brand-blue-deep) 100%);
  }
  .brand-panel__wash {
    position: absolute;
    left: 0;
    bottom: 40px;
    width: 260px;
    height: 200px;
    background: radial-gradient(ellipse at 30% 60%, rgba(255,255,255,0.22) 0%, rgba(255,255,255,0) 70%);
  }
  .brand-name {
    position: absolute;
    left: 28px;
    top: 34px;
    display: flex;
    align-items: center;
    gap: 12px;
    font-family: "Open Sans", sans-serif;
    font-weight: 600;
    font-size: 25px;
    line-height: 1.1;
    color: var(--white);
    text-transform: uppercase;
    letter-spacing: 0.5px;
  }
  .brand-name__dot {
    width: 46px;
    height: 46px;
    border-radius: 50%;
    background: var(--white);
    flex: none;
  }
  .tagline {
    position: absolute;
    left: 24px;
    bottom: 34px;
    font-family: "Satisfy", cursive;
    font-size: 30px;
    color: var(--white);
    letter-spacing: 1px;
  }
  .divider {
    position: absolute;
    left: 365px;
    top: 0;
    width: 4px;
    height: 100%;
    background: var(--brand-blue);
  }
  .content-wash {
    position: absolute;
    left: 560px;
    top: -40px;
    width: 560px;
    height: 420px;
    background: radial-gradient(ellipse at 55% 40%, var(--wash) 0%, rgba(233,240,248,0) 68%);
  }
  .contact {
    position: absolute;
    right: 52px;
    bottom: 34px;
    text-align: right;
  }
  .contact__phone {
    font-family: "Exo 2", sans-serif;
    font-size: 35px;
    color: var(--brand-blue);
    letter-spacing: 1px;
    margin-bottom: 8px;
  }
  .contact__address {
    font-family: "Open Sans", sans-serif;
    font-weight: 300;
    font-size: 21px;
    color: var(--ink-grey);
  }
</style>
</head>
<body>
  <main class="stage">
    <section class="envelope" aria-label="The Orbit Dental Works DL envelope">
      <div class="brand-panel">
        <div class="brand-panel__wash"></div>
        <div class="brand-name">
          <span class="brand-name__dot"></span>
          <span>The Orbit<br>Dental Works</span>
        </div>
        <p class="tagline">a reason to smile</p>
      </div>
      <div class="divider"></div>
      <div class="content-wash"></div>
      <div class="contact">
        <p class="contact__phone">02 4817 3306</p>
        <p class="contact__address">Suite 4, 61 Holloway Street, Bellmore NSW 2287</p>
      </div>
    </section>
  </main>
</body>
</html>
```